Business Card Design

We need a new business card for our restaurant/motel as we are new owners. Our business is in a small community in a rainforest north of Townsville, Queensland AUSTRALIA and we are on a mountain 3000 feet above sea level. Visitors come here to see the wide variety of birds (This area is especially noted for the cassowary and riflebird), travel the many bush walks and enjoy the cooler climate. We would like you to use as the main colours blue and green - the buildings are painted in those colours and reflect the green for the forest and blue for the rain/sky. Yellow could also be used. The card should be bright and cheerful.
Industry/Entity Type
Travel
Contact Information for Business Card
Ferncliff Lodge Warrabee
Licensed Café/ Restaurant & Motel
14 Tallowood Lane KORRINGA Qld 4829
Ph: 07 4912 3057 Fax: 07 49123094
reception@ferncliffwarrabee.example
www.ferncliffwarrabee.example
like us on friendsgate
Look and feel
Each slider illustrates characteristics of the customer's brand and the style your logo design should communicate.

```html
<!DOCTYPE html>
<html lang="en">
<head>
<meta charset="utf-8">
<title>Ferncliff Lodge Warrabee – Business Card</title>
<link rel="stylesheet" href="https://fonts.googleapis.com/css2?family=Parisienne&family=Arimo:wght@400&display=swap">
<style>
  :root {
    --forest-green: #2f8f45;
    --leaf-green: #4fae4a;
    --sky-blue: #2d86c6;
    --deep-blue: #1f5fa3;
    --sun-yellow: #f6d743;
    --ink-light: #ffffff;
    --ink-soft: #fff3b8;
    --shadow: rgba(0, 40, 30, 0.55);
  }
  html, body {
    margin: 0;
    padding: 0;
    width: 1200px;
    height: 741px;
    overflow: hidden;
  }
  .card {
    position: relative;
    width: 1200px;
    height: 741px;
    overflow: hidden;
    background: linear-gradient(160deg, var(--leaf-green) 0%, var(--forest-green) 45%, var(--sky-blue) 100%);
  }
  .card__glow {
    position: absolute;
    inset: 0;
    background: radial-gradient(ellipse at 50% 40%, rgba(255, 255, 255, 0.16) 0%, rgba(255, 255, 255, 0) 60%);
  }
  .logo-mark {
    position: absolute;
    left: 0;
    top: 160px;
    width: 1200px;
    display: flex;
    justify-content: center;
    align-items: center;
    gap: 18px;
  }
  .logo-mark__dot {
    width: 64px;
    height: 64px;
    border-radius: 50%;
    background: var(--sun-yellow);
  }
  .logo-mark__name {
    font-family: "Arimo", Arial, sans-serif;
    font-size: 30px;
    font-weight: 400;
    color: var(--ink-light);
    line-height: 1;
  }
  .brand {
    position: absolute;
    left: 0;
    width: 1200px;
    text-align: center;
    color: var(--ink-light);
    font-family: "Parisienne", cursive;
    text-shadow: 3px 4px 5px var(--shadow);
    margin: 0;
    font-weight: 400;
    white-space: nowrap;
  }
  .brand__name {
    top: 316px;
    font-size: 50px;
    letter-spacing: 7px;
    line-height: 1;
  }
  .brand__tagline {
    top: 386px;
    font-size: 32px;
    letter-spacing: 3.5px;
    line-height: 1;
    color: var(--ink-soft);
  }
  .contact {
    position: absolute;
    left: 0;
    width: 1200px;
    text-align: center;
    font-family: "Arimo", Arial, sans-serif;
    font-size: 16.5px;
    letter-spacing: -0.6px;
    color: var(--ink-light);
    text-shadow: 2px 2px 3px var(--shadow);
    margin: 0;
    line-height: 1;
    white-space: nowrap;
  }
  .contact__main { top: 509px; }
  .contact__web { top: 530px; }
  .contact__sep { margin: 0 5px; color: var(--sun-yellow); }
  .social-square {
    position: absolute;
    left: 577px;
    top: 557px;
    width: 47px;
    height: 47px;
    border-radius: 6px;
    background: var(--deep-blue);
    box-shadow: 2px 3px 5px var(--shadow);
  }
  .altitude {
    top: 618px;
    color: var(--ink-soft);
  }
</style>
</head>
<body>
  <main class="card">
    <div class="card__glow"></div>

    <div class="logo-mark">
      <span class="logo-mark__dot" aria-hidden="true"></span>
      <span class="logo-mark__name">Ferncliff Lodge Warrabee</span>
    </div>

    <h1 class="brand brand__name">Ferncliff Lodge Warrabee</h1>
    <p class="brand brand__tagline">Licensed Cafe Restaurant&nbsp; Motel</p>

    <p class="contact contact__main">14 Tallowood Lane KORRINGA Qld 4829<span class="contact__sep">•</span>Ph: 07 4912 3057 Fax: 07 49123094<span class="contact__sep">•</span>reception@ferncliffwarrabee.example</p>
    <p class="contact contact__web">www.ferncliffwarrabee.example like us on friendsgate</p>

    <div class="social-square" aria-hidden="true"></div>

    <p class="contact altitude">3000 feet above sea level</p>
  </main>
</body>
</html>
```